Need Business Cards for my Business

email address: rkpmarlowhollowworks@vendrimail.com
web address: rkpmarlowhollowworks.net
Slogan: We offer various QVN licenses
Rowland K. Pemberly
Please stick with colors of Company Logo
would like the card to be more of the color example of the logo.
If you need PDF copy of logo email me at the above account.
Creative control rests with you.

Industry/Entity Type

Business

Contact Information for Business Card

I am a minimalist, but would like something to pop and stand out amongst other cards, make it memorable.

Font styles to use
Serif
Decorative
Script

```html
<!DOCTYPE html>
<html lang="en">
<head>
<meta charset="utf-8">
<title>RKP Marlow Hollow Works — Business Card</title>
<link href="https://fonts.googleapis.com/css2?family=Source+Sans+3:wght@400;600&display=swap" rel="stylesheet">
<style>
  :root {
    --backdrop: #dedede;
    --frame-red: #e3262b;
    --frame-red-deep: #c1212f;
    --card-white: #ffffff;
    --card-dark: #2d2d2d;
    --mark-grey: #d3d3d4;
    --mark-grey-dark: #4a4848;
    --brand-navy: #1c3050;
    --accent-red: #d3292c;
    --text-light: #f2f2f2;
  }
  * { margin: 0; padding: 0; box-sizing: border-box; }
  html, body {
    width: 1200px; height: 1000px; overflow: hidden;
    background: var(--backdrop);
    font-family: "Source Sans 3", "Myriad Pro", Arial, sans-serif;
  }
  .card {
    position: absolute; left: 227px; width: 746px; height: 426px;
    background: linear-gradient(90deg, var(--frame-red), var(--frame-red-deep));
    padding: 20px;
  }
  .card--front { top: 49px; }
  .card--back { top: 525px; }
  .card__face {
    position: relative; width: 100%; height: 100%; overflow: hidden;
  }
  .card--front .card__face { background: var(--card-white); }
  .card--back .card__face { background: var(--card-dark); }
  .card__decor {
    position: absolute; border-radius: 50%;
  }
  .card--front .card__decor {
    left: 170px; top: 20px; width: 420px; height: 420px; background: var(--mark-grey); opacity: .5;
  }
  .card--back .card__decor {
    left: 330px; top: 20px; width: 360px; height: 360px; background: var(--mark-grey-dark); opacity: .75;
  }
  .brand {
    position: absolute; left: 0; right: 0; top: 164px;
    display: flex; align-items: center; justify-content: center; gap: 16px;
  }
  .brand__square { width: 34px; height: 34px; background: var(--accent-red); }
  .brand__name {
    font-weight: 600; font-size: 44px; line-height: 1; color: var(--brand-navy); letter-spacing: .5px;
  }
  .holder {
    position: absolute; left: 21px; top: 148px;
    display: flex; align-items: baseline; gap: 10px;
  }
  .holder__name { color: var(--accent-red); font-size: 19px; }
  .holder__title { color: var(--text-light); font-size: 16px; }
  .rule {
    position: absolute; left: 8px; right: 21px; top: 183px; height: 2px; background: var(--accent-red);
  }
  .contact {
    position: absolute; left: 17px; right: 22px; top: 196px;
    display: flex; justify-content: space-between;
    color: var(--text-light); font-size: 16px;
  }
</style>
</head>
<body>
  <section class="card card--front">
    <div class="card__face">
      <div class="card__decor" aria-hidden="true"></div>
      <div class="brand">
        <span class="brand__square"></span>
        <span class="brand__name">RKP Marlow Hollow Works</span>
      </div>
    </div>
  </section>

  <section class="card card--back">
    <div class="card__face">
      <div class="card__decor" aria-hidden="true"></div>
      <div class="holder">
        <span class="holder__name">Rowland K. Pemberly</span>
        <span class="holder__title">Director</span>
      </div>
      <div class="rule"></div>
      <div class="contact">
        <span class="contact__direct">555-014-2871/rkpmarlowhollowworks@vendrimail.com</span>
        <span class="contact__web">rkpmarlowhollowworks.net</span>
      </div>
    </div>
  </section>
</body>
</html>
```